Brivane - Business Cards for a new venture

create business card for a startup classified business dealing in construction materials, the cards need to have a professional look but modern, more serious than playful, one of the samples must include the official font (attached), please explore using the official colors in the company's logo

Target Market(s)

Energy sector

Contact Information for Business Card

Font styles to use
Other font styles liked:
• suissnord

Requirements
Must have
• corporate colors (in logo attached)
Nice to have
• Official font (in one of the samples) font is : suissnord
Should not have
• Cartoonish look

```html
<!DOCTYPE html>
<html lang="en">
<head>
<meta charset="utf-8">
<title>Brivane – Business Card</title>
<link rel="stylesheet" href="https://fonts.googleapis.com/css2?family=Orbitron:wght@400;500&display=swap">
<style>
  :root {
    --page-bg: #e4e5e8;
    --card-white: #f3f3f2;
    --brand-blue: #0d4784;
    --brand-grey: #b7bac4;
    --name-grey: #8b8e9e;
    --ink-light: #ffffff;
  }
  * { margin: 0; padding: 0; box-sizing: border-box; }
  html, body {
    width: 1200px; height: 900px; overflow: hidden;
    background: var(--page-bg);
    font-family: "Orbitron", sans-serif;
  }
  .card {
    position: absolute; left: 50px; top: 137px;
    width: 1100px; height: 625px;
    background: var(--card-white);
    box-shadow: 0 6px 18px rgba(0,0,0,0.12);
    overflow: hidden;
  }
  .card-panels { position: absolute; inset: 0; width: 100%; height: 100%; }
  .brand-name {
    position: absolute; left: 0; width: 500px; top: 330px;
    text-align: center;
    font-size: 40px; font-weight: 500; letter-spacing: 4px;
    color: var(--name-grey); text-transform: uppercase;
  }
  .holder { position: absolute; left: 631px; color: var(--ink-light); }
  .holder-name { top: 84px; font-size: 40px; font-weight: 400; letter-spacing: 1px; }
  .holder-role { top: 146px; font-size: 20px; letter-spacing: 2px; }
  .contact-list { position: absolute; left: 640px; top: 0; list-style: none; color: var(--ink-light); }
  .contact-item {
    position: absolute; left: 0; display: flex; align-items: flex-start; gap: 18px;
    font-size: 21px; letter-spacing: 1.5px; white-space: nowrap; line-height: 31px;
  }
  .contact-icon { width: 24px; height: 24px; flex: none; margin-top: 3px; fill: var(--ink-light); }
  .phone-mobile { top: 255px; }
  .phone-office { top: 293px; }
  .address { top: 369px; }
  .email { top: 483px; }
  .web { top: 528px; }
</style>
</head>
<body>
  <div class="card">
    <svg class="card-panels" viewBox="0 0 985 562" preserveAspectRatio="none" aria-hidden="true">
      <polygon points="397,0 442,212 512,277 442,337 407,562 985,562 985,0" fill="var(--brand-grey)"/>
      <polygon points="415,0 460,212 530,277 460,337 430,562 985,562 985,0" fill="var(--brand-blue)"/>
    </svg>

    <div class="brand-name">Brivane</div>

    <div class="holder holder-name">Full Name</div>
    <div class="holder holder-role">Designation</div>

    <ul class="contact-list">
      <li class="contact-item phone-mobile">
        <svg class="contact-icon" viewBox="0 0 24 24"><path d="M6.6 10.8a15 15 0 0 0 6.6 6.6l2.2-2.2a1 1 0 0 1 1-.25 11 11 0 0 0 3.6.6 1 1 0 0 1 1 1V20a1 1 0 0 1-1 1A17 17 0 0 1 3 4a1 1 0 0 1 1-1h3.5a1 1 0 0 1 1 1c0 1.25.2 2.45.6 3.6a1 1 0 0 1-.25 1z"/></svg>
        <span>(+1) 123 4567 890</span>
      </li>
      <li class="contact-item phone-office">
        <svg class="contact-icon" viewBox="0 0 24 24"><path d="M3 3h5v18H3zM10 5h11v16H10zM12 7v4h7V7zM12 13h2v2h-2zM15.5 13h2v2h-2zM12 16.5h2v2h-2zM15.5 16.5h2v2h-2z" fill-rule="evenodd"/></svg>
        <span>(+1) 123 4567 890</span>
      </li>
      <li class="contact-item address">
        <svg class="contact-icon" viewBox="0 0 24 24"><path d="M12 2a7 7 0 0 0-7 7c0 5 7 13 7 13s7-8 7-13a7 7 0 0 0-7-7zm0 9.5A2.5 2.5 0 1 1 12 6.5a2.5 2.5 0 0 1 0 5z"/></svg>
        <span>Address Line 1<br>Address Line 2</span>
      </li>
      <li class="contact-item email">
        <svg class="contact-icon" viewBox="0 0 24 24"><path d="M2 5h20v14H2zm2 2v.5l8 5 8-5V7zm0 2.8V17h16V9.8l-8 5z" fill-rule="evenodd"/></svg>
        <span>brivane@info.com</span>
      </li>
      <li class="contact-item web">
        <svg class="contact-icon" viewBox="0 0 24 24"><circle cx="12" cy="12" r="9" fill="none" stroke="#fff" stroke-width="1.8"/><ellipse cx="12" cy="12" rx="4" ry="9" fill="none" stroke="#fff" stroke-width="1.5"/><path d="M3 12h18M5 7.5h14M5 16.5h14" stroke="#fff" stroke-width="1.5"/></svg>
        <span>www.brivane.com</span>
      </li>
    </ul>
  </div>
</body>
</html>
```